Lumaform website scandinavian interior design

Existing website: http://lumaform-example.no/

Webdesign for interior designer Ragna Tvedtholm. The company name is Lumaform. Scandinavian interiør is known to be simple and elegant. The website will be in Norwegian, we are working on the text. The website needs to have a few more pages than just the front page. Here are the different titles of the pages:

1. Hjem
2. Om Lumaform
3. Tjenester og priser
4.. Kontakt oss

There should be Facebook and Instagram icons somewhere at the bottom of the website.

The logo we want to use is attached (pink with black print, see attachment )

We have attached images for inspiration. We want to use some of these colors. The color in the logo, The style should be elegant, modern and delicate.

It is imprtant that the website is user friendly.

Target Market(s)

People who want to decorate their home
Companies and public sector who need to redecorate

Industry/Entity Type

Interior Designer

Coding

Coded - Design and coding required

Number of Pages Required

5+ page

Font styles to use
Other font styles liked:
• see example in the logo breakdown

Requirements
Must have
• Elegant, modern and delicate design
Images of design, see examples attached
Colors similar to the pictures
Should not have
• Too bright colors
Pictures of people

```html
<!DOCTYPE html>
<html lang="no">
<head>
<meta charset="utf-8">
<title>Lumaform – interiørdesign</title>
<link href="https://fonts.googleapis.com/css2?family=Montserrat:wght@400;500;600;700&family=Open+Sans:wght@400;600&display=swap" rel="stylesheet">
<style>
:root{
  --blush:#efd8d4;
  --blush-deep:#e6c7c2;
  --ink:#1d1716;
  --ink-soft:#3a302e;
  --muted:#8d8684;
  --line:#cfc8c6;
  --paper:#ffffff;
  --band:#3a2722;
}
*{margin:0;padding:0;box-sizing:border-box}
html,body{width:1200px;height:3448px;overflow:hidden}
body{background:var(--blush);font-family:"Open Sans",Arial,sans-serif;color:var(--ink);position:relative}
.page{position:absolute;left:48px;top:0;width:1104px;height:3220px;background:var(--paper)}
.abs{position:absolute}
.ghost-word{position:absolute;font-family:"Montserrat",Arial,sans-serif;font-weight:700;font-size:260px;letter-spacing:10px;color:#f4f1f0;line-height:1;white-space:nowrap}
.brand{left:200px;top:40px;display:flex;align-items:center;gap:12px}
.brand-mark{width:22px;height:22px;border-radius:50%;background:var(--blush-deep)}
.brand-name{font-family:"Montserrat",Arial,sans-serif;font-weight:600;font-size:26px;color:var(--ink)}
.hero-photo{left:540px;top:-120px;width:740px;height:680px;border-radius:50%;background:linear-gradient(160deg,#e9ecef 0%,#c9ccd0 45%,#6f6560 80%,#3e3430 100%);overflow:hidden}
.nav{left:680px;top:60px;display:flex;gap:26px;font-family:"Montserrat",Arial,sans-serif;font-size:15px;font-weight:500;color:var(--ink)}
.hero-title{left:188px;top:216px;width:420px;font-family:"Montserrat",Arial,sans-serif;font-weight:700;font-size:42px;line-height:1.12}
.hero-text{left:188px;top:366px;width:380px;font-size:12px;line-height:1.6;color:var(--ink-soft)}
.btn{left:188px;top:452px;padding:8px 20px;background:var(--ink);color:#fff;border-radius:20px;font-family:"Montserrat",Arial,sans-serif;font-size:11px;font-weight:600;text-transform:uppercase;letter-spacing:.5px}
.scroll-cue{left:590px;top:490px}
.photo{position:absolute}
.living{left:188px;top:608px;width:824px;height:480px;background:linear-gradient(180deg,#f1f1f0 0%,#e3e1de 55%,#b9b4ae 100%)}
.eyebrow{left:188px;top:1150px;font-size:12px;color:var(--muted)}
.section-title{font-family:"Montserrat",Arial,sans-serif;font-weight:700;color:var(--ink)}
.spazi{left:188px;top:1170px;width:460px;font-size:40px;line-height:1.12}
.lounge{left:188px;top:1368px;width:528px;height:412px;background:linear-gradient(180deg,#f4f4f3 0%,#e6e6e5 60%,#2f3740 100%)}
.feature-head{left:584px;top:1372px;display:flex;align-items:center;gap:14px;font-family:"Montserrat",Arial,sans-serif;font-weight:700;font-size:19px;letter-spacing:.5px}
.feature-head::after{content:"";width:60px;height:2px;background:var(--ink)}
.feature-text{left:736px;top:1420px;width:290px;font-size:11px;line-height:1.7;color:var(--muted)}
.band{left:0;top:1960px;width:1200px;height:460px;background:linear-gradient(90deg,#4a332c 0%,#2c1e1a 45%,#3a2722 70%,#5a3f36 100%)}
.band-photo{left:400px;top:1920px;width:448px;height:360px;background:linear-gradient(135deg,#f3efe9 0%,#dcc9b2 50%,#b48a62 100%)}
.featured-card{left:172px;top:1960px;width:240px;height:360px;background:rgba(246,242,240,.96);padding:40px 28px}
.featured-card .label{font-family:"Montserrat",Arial,sans-serif;font-size:9px;letter-spacing:2px;color:var(--muted);text-transform:uppercase}
.featured-card .name{margin-top:14px;font-family:"Montserrat",Arial,sans-serif;font-size:21px;line-height:1.3;color:var(--ink)}
.card-nav{position:absolute;left:28px;bottom:28px;display:flex;gap:22px;font-size:11px;font-family:"Montserrat",Arial,sans-serif;letter-spacing:1px;color:var(--ink-soft)}
.band-text{left:360px;top:2318px;width:640px;font-size:11px;line-height:1.6;color:#e9dcd8}
.projects-title{left:188px;top:2500px;font-size:54px}
.projects-sub{left:188px;top:2574px;width:440px;font-size:12px;line-height:1.5;color:var(--muted)}
.vases{left:188px;top:2640px;width:572px;height:244px;background:linear-gradient(180deg,#3c3f44 0%,#2b2d31 65%,#6e5b46 100%)}
.note-tile{left:188px;top:2884px;width:332px;height:296px;background:#f3dedb;text-align:center;padding-top:80px}
.note-tile p{margin:18px auto 0;width:220px;font-size:10px;line-height:1.5;color:var(--ink-soft);text-transform:uppercase;letter-spacing:.5px}
.room-small{left:520px;top:2884px;width:240px;height:296px;background:linear-gradient(180deg,#eceae6 0%,#d8d2c9 60%,#9a8c7b 100%)}
.side-a{left:760px;top:2640px;width:252px;height:118px;background:linear-gradient(180deg,#f1ede8 0%,#d9cfc6 100%)}
.side-b{left:760px;top:2758px;width:252px;height:210px;background:linear-gradient(135deg,#e8e0ea 0%,#cbb9c4 50%,#7d6a63 100%)}
.side-c{left:760px;top:2968px;width:252px;height:212px;background:linear-gradient(180deg,#eee9e3 0%,#c9bdb0 60%,#6c5a4c 100%)}
.plus-box{left:716px;top:2950px;width:26px;height:26px;background:var(--ink)}
.footer{left:0;top:3220px;width:1200px;height:228px;background:var(--blush)}
.f-brand{left:188px;top:3270px}
.f-col{top:3262px;font-size:11px;line-height:1.6;color:var(--ink-soft)}
.f-col strong{display:block;font-family:"Montserrat",Arial,sans-serif;font-size:12px;color:var(--ink);margin-bottom:6px}
.newsletter{left:900px;top:3262px;width:170px}
.newsletter strong{font-family:"Montserrat",Arial,sans-serif;font-size:12px;display:block;margin-bottom:10px}
.signup{display:flex;height:22px}
.signup span{flex:1;background:#fff}
.signup b{width:48px;background:var(--ink);color:#fff;font-size:8px;display:flex;align-items:center;justify-content:center;font-weight:600}
.socials{display:flex;gap:10px;margin-top:12px}
.f-bottom{left:188px;top:3410px;width:824px;display:flex;justify-content:space-between;font-size:9px;color:var(--ink-soft)}
.f-bottom span+span{margin-left:18px}
</style>
</head>
<body>
<main class="page"></main>

<div class="ghost-word" style="left:40px;top:560px">WE WORK</div>
<div class="ghost-word" style="left:60px;top:2420px">WORKS</div>

<div class="abs hero-photo" role="img" aria-label="Lyst kjøkken med hvite stoler rundt et mørkt bord"></div>

<header>
  <div class="abs brand"><span class="brand-mark"></span><span class="brand-name">Lumaform</span></div>
  <nav class="abs nav"><span>Hjem</span><span>Om Lumaform</span><span>Tjenester og priser</span><span>Kontakt oss</span></nav>
</header>

<section>
  <h1 class="abs hero-title">Trenger du hjelp til utvikling av interiørmiljøer?</h1>
  <p class="abs hero-text">Hos Lumaform får du personlig rådgivning fra idé til ferdig rom. Vi skaper lyse, rolige og funksjonelle hjem og arbeidsplasser i skandinavisk stil, med omtanke for materialer, farger og lys i hvert eneste prosjekt.</p>
  <span class="abs btn">Lær mer</span>
  <svg class="abs scroll-cue" width="20" height="24" viewBox="0 0 20 24"><path d="M10 2v18M5 15l5 5 5-5" stroke="#1d1716" stroke-width="1.5" fill="none"/></svg>
</section>

<div class="photo living" role="img" aria-label="Lys stue med grå lenestol, lave skap og pendellamper"></div>

<section>
  <p class="abs eyebrow">Lorem ipsum dolor sit amet, consectetur adipiscing elit</p>
  <h2 class="abs section-title spazi">Abitare spazi aperti nella luce</h2>
  <div class="photo lounge" role="img" aria-label="Lyst rom med stor grønn plante og mørke sittemøbler"></div>
  <h3 class="abs feature-head">HIGH TECH &amp; HIGH DESIGN</h3>
  <p class="abs feature-text">Vi kombinerer smarte løsninger med tidløs design. Hvert rom planlegges nøye, slik at teknologi, lys og møbler fungerer sammen i en helhet som er enkel å leve med, både i dag og i årene som kommer.</p>
</section>

<section>
  <div class="abs band" role="img" aria-label="Varmt, mørkt interiør med trevegger og sofa"></div>
  <div class="abs band-photo" role="img" aria-label="Lys spiseplass med trappeløp og trebord"></div>
  <div class="abs featured-card">
    <p class="label">Featured project</p>
    <p class="name">Fjordlys<br>Bolig</p>
    <div class="card-nav"><span>PREV</span><span>—</span><span>NEXT</span></div>
  </div>
  <p class="abs band-text">Et helhetlig prosjekt der åpne flater, naturlige materialer og varmt lys skaper et rolig hjem. Vi fulgte kunden fra første skisse til ferdig innflytting, med fokus på detaljer.</p>
</section>

<section>
  <h2 class="abs section-title projects-title">Our Projects</h2>
  <p class="abs projects-sub">Vi er opptatt av å skape noe som gir glede i hverdagen. Her er et utvalg av våre prosjekter.</p>
  <div class="photo vases" role="img" aria-label="Keramiske vaser på en hylle mot mørk vegg"></div>
  <div class="abs note-tile">
    <svg width="24" height="24" viewBox="0 0 24 24"><path d="M12 2v20M2 12h20" stroke="#1d1716" stroke-width="1.5"/></svg>
    <p>Se flere prosjekter fra våre kunder</p>
  </div>
  <div class="photo room-small" role="img" aria-label="Lyst rom med sofa og bilder på veggen"></div>
  <div class="photo side-a" role="img" aria-label="Hvit hylle med dekorasjoner"></div>
  <div class="photo side-b" role="img" aria-label="Soverom i pastell med kunst på veggen"></div>
  <div class="photo side-c" role="img" aria-label="Stue med lampe og lenestol"></div>
  <div class="abs plus-box"><svg width="26" height="26" viewBox="0 0 26 26"><path d="M13 7v12M7 13h12" stroke="#fff" stroke-width="1.5"/></svg></div>
</section>

<footer>
  <div class="abs footer"></div>
  <div class="abs brand f-brand"><span class="brand-mark" style="background:#fff"></span><span class="brand-name">Lumaform</span></div>
  <div class="abs f-col" style="left:400px"><strong>Ragna Tvedtholm</strong>Storgata 14, 2. etg<br>Postboks 220<br>0155 Oslo</div>
  <div class="abs f-col" style="left:660px">Tlf: +47 400 00 000<br>Mob: +47 900 00 000<br>Web: lumaform-example.no<br><br>Følg oss på sosiale medier</div>
  <div class="abs newsletter">
    <strong>Newsletter Sign Up</strong>
    <div class="signup"><span></span><b>SEND</b></div>
    <div class="socials"><svg width="14" height="14"><rect width="14" height="14" fill="#1d1716"/></svg><svg width="14" height="14"><rect width="14" height="14" fill="#1d1716"/></svg></div>
  </div>
  <div class="abs f-bottom"><span>© Lumaform. All Rights Reserved.</span><div><span>Terms of Use</span><span>Privacy Policy</span></div></div>
</footer>
</body>
</html>
```